Updating Company Website with New Brand Collateral

Needing to update the current website to the new company name and brand.
Square Space platform

A home landing page with an additional secure blog site.

Current website at: https://www.quillbrookco.com/

Once the basic design and flow it set up, I will add content in after the fact.

Like Website like:
https://www.kowelgrp.com/
https://www.xmfhospitality.com/
https://www.vorlenddentalservices.com/

Industry/Entity Type

Small Business

Coding

Coded - Design and coding required

Number of Pages Required

5+ page

Font styles to use
Sans Serif

Requirements
Must have
• Clear, clean design that is easy to navigate.
Home page
About us
Locations
Blog/News
Contact us
Join our team
Nice to have
• Interactive Map of locations

```html
<!DOCTYPE html>
<html lang="en">
<head>
<meta charset="utf-8">
<title>ORVA — Home</title>
<link href="https://fonts.googleapis.com/css2?family=Fira+Sans:wght@400;500;600&family=Lato:wght@400;700&display=swap" rel="stylesheet">
<style>
:root{
  --green-dark:#1f5a4c;
  --green-btn:#1f4f46;
  --teal:#3f9c8a;
  --blue:#137aa0;
  --pale:#c7d8d4;
  --ink:#222;
  --footer:#1e1e1e;
  --map:#6e90dc;
}
*{margin:0;padding:0;box-sizing:border-box}
html,body{width:1200px;height:3686px;overflow:hidden;background:#fff}
body{position:relative;font-family:"Lato",sans-serif;color:var(--ink)}
.abs{position:absolute}
.shapes{position:absolute;left:0;top:0}
.brand{left:143px;top:50px;font-family:"Fira Sans",sans-serif;font-weight:600;font-size:46px;color:var(--green-dark);letter-spacing:1px;display:flex;align-items:center;gap:12px}
.brand .dot{width:22px;height:22px;background:var(--teal)}
.btn{position:absolute;display:flex;align-items:center;justify-content:center;font-family:"Fira Sans",sans-serif;font-weight:500;font-size:16px;color:#fff;background:var(--blue);text-transform:uppercase}
.btn.dark{background:var(--green-btn)}
.nav{left:453px;top:108px;display:flex;font-family:"Fira Sans",sans-serif;font-size:16px}
.nav a{position:absolute;white-space:nowrap;color:var(--ink);text-decoration:none}
.nav a.active{color:var(--blue)}
.hero-title{left:0;width:1200px;top:322px;text-align:center;color:#fff;font-family:"Fira Sans",sans-serif;font-weight:600;font-size:41px;line-height:48px;text-transform:uppercase}
.chev{position:absolute;top:370px}
h2.section{position:absolute;font-family:"Fira Sans",sans-serif;font-weight:600;font-size:40px;color:var(--green-dark);text-transform:uppercase;line-height:1}
.copy{position:absolute;font-size:14.5px;line-height:29px;color:#333}
.services{position:absolute;left:641px;top:1543px;list-style:none}
.services li{display:flex;align-items:center;height:59px;font-family:"Fira Sans",sans-serif;font-weight:500;font-size:28px;color:var(--blue);gap:16px}
.card{position:absolute;top:1991px;width:296px;height:297px;background:#fff;box-shadow:0 2px 10px rgba(0,0,0,.15)}
.card .pic{margin:9px;height:136px}
.card .date{margin:22px 0 0 22px;font-family:"Fira Sans",sans-serif;font-size:15px;color:#333;text-transform:uppercase}
.card .title{margin:12px 20px 0 22px;font-family:"Fira Sans",sans-serif;font-weight:500;font-size:16px;line-height:25px;color:var(--blue)}
.field{position:absolute;border:1px solid #aaa;font-size:11px;color:#555;padding:12px 14px}
.foot-links{left:143px;top:3551px;font-size:12px;color:#fff;word-spacing:2px}
.foot-copy{left:143px;top:3584px;font-size:12px;color:#fff}
</style>
</head>
<body>

<svg class="shapes" width="1200" height="3686" viewBox="0 0 1200 3686">
  <defs>
    <linearGradient id="heroTone" x1="0" y1="0" x2="1" y2="1">
      <stop offset="0" stop-color="#5a3a1c"/><stop offset=".5" stop-color="#9a5a24"/><stop offset="1" stop-color="#6b2c14"/>
    </linearGradient>
    <linearGradient id="handTone" x1="0" y1="0" x2="1" y2="1">
      <stop offset="0" stop-color="#2f3e58"/><stop offset=".6" stop-color="#7a5a48"/><stop offset="1" stop-color="#a9c0d8"/>
    </linearGradient>
    <linearGradient id="cafeTone" x1="0" y1="0" x2="1" y2="1">
      <stop offset="0" stop-color="#c8a27a"/><stop offset=".5" stop-color="#6b4a34"/><stop offset="1" stop-color="#8a3c30"/>
    </linearGradient>
    <linearGradient id="phoneTone" x1="0" y1="0" x2="1" y2="1">
      <stop offset="0" stop-color="#e6ebef"/><stop offset=".6" stop-color="#8aa6bf"/><stop offset="1" stop-color="#dfe6ec"/>
    </linearGradient>
    <linearGradient id="mapTone" x1="0" y1="0" x2="1" y2="0">
      <stop offset="0" stop-color="#6e90dc"/><stop offset=".2" stop-color="#a9c99a"/><stop offset=".55" stop-color="#b9d3a4"/><stop offset=".8" stop-color="#6e90dc"/>
    </linearGradient>
  </defs>

  <g role="img" aria-label="Photo of a warmly lit restaurant bar interior">
    <polygon points="0,157 1200,157 1200,622 1058,708 0,615" fill="url(#heroTone)"/>
  </g>
  <polygon points="0,615 1058,708 1200,622 1200,650 1070,716 1045,716" fill="var(--teal)"/>

  <g role="img" aria-label="Photo of a smiling businessman shaking hands">
    <polygon points="601,1037 1200,687 1200,1230" fill="url(#handTone)"/>
  </g>

  <polygon points="350,1637 0,1838 0,1995" fill="var(--pale)"/>
  <g role="img" aria-label="Photo of a modern restaurant dining room with pendant lamps">
    <polygon points="0,1230 541,1535 0,1838" fill="url(#cafeTone)"/>
  </g>

  <polygon points="1200,2245 862,2539 1200,2367" fill="var(--pale)"/>
  <g role="img" aria-label="Photo of a smiling man talking on the phone">
    <polygon points="659,2656 1200,2417 1200,2889" fill="url(#phoneTone)"/>
  </g>

  <g role="img" aria-label="Map of North America showing office locations">
    <polygon points="0,3053 143,2972 1200,3062 1200,3518 0,3518" fill="url(#mapTone)"/>
  </g>
  <polygon points="0,3053 143,2960 1200,3048 1200,3062 143,2972" fill="var(--teal)"/>
  <g fill="#fff" stroke="#ccc">
    <rect x="340" y="3145" width="54" height="54"/>
    <rect x="485" y="3090" width="54" height="54"/>
    <rect x="700" y="3255" width="54" height="54"/>
  </g>

  <rect x="0" y="3518" width="1200" height="114" fill="var(--footer)"/>
  <rect x="0" y="3632" width="1200" height="54" fill="var(--teal)"/>
  <polygon points="830,3686 997,3332 1030,3686" fill="var(--teal)"/>
  <polygon points="940,3540 1030,3540 1030,3686 880,3686" fill="var(--green-btn)"/>
  <polygon points="1030,3686 1098,3490 1200,3640 1200,3686" fill="var(--blue)"/>
  <circle cx="993" cy="3579" r="10" fill="#fff"/>
  <circle cx="1044" cy="3579" r="10" fill="#fff"/>
</svg>

<div class="abs brand"><span class="dot"></span>ORVA</div>
<div class="btn dark" style="left:928px;top:31px;width:127px;height:43px">Get Started</div>
<nav class="abs nav">
  <a class="active" style="left:0">Home</a>
  <a style="left:85px">About us</a>
  <a style="left:192px">Locations</a>
  <a style="left:304px">News</a>
  <a style="left:385px">Contact Us</a>
  <a style="left:505px">Join the Team</a>
</nav>

<div class="abs hero-title">Vestibulum condimentum<br>risus posuere cursus</div>
<div class="btn dark" style="left:540px;top:433px;width:119px;height:40px">Read More</div>
<svg class="chev" style="left:54px" width="20" height="30" viewBox="0 0 20 30"><path d="M16 3 4 15l12 12" fill="none" stroke="#fff" stroke-width="4"/></svg>
<svg class="chev" style="left:1124px" width="20" height="30" viewBox="0 0 20 30"><path d="M4 3l12 12L4 27" fill="none" stroke="#fff" stroke-width="4"/></svg>

<h2 class="section" style="left:143px;top:792px">Welcome to ORVA</h2>
<p class="copy" style="left:143px;top:844px;width:420px">Nulla tristique posuere molestie. Aliquam erat volutpat. Etiam quis aliquet risus. Duis ornare erat eget magna dapibus, in accumsan quam pharetra. Nam tempus, quam in bibendum vulputate, sapien dolor viverra nisl, vitae euismod elit turpis et nulla. Aliquam erat volutpat. Pellentesque blandit lacus eget nunc faucibus, et tincidunt eros viverra. Phasellus consequat sagittis nisi suscipit feugiat.</p>
<div class="btn" style="left:143px;top:1060px;width:119px;height:43px">Read More</div>

<h2 class="section" style="left:641px;top:1301px">What we do</h2>
<p class="copy" style="left:641px;top:1353px;width:418px">Cras eget leo sed nunc hendrerit ultricies eu at nisl. Praesent iaculis faucibus urna sit amet lacinia. Maecenas consequat justo enim, ac mattis massa imperdiet quis. Fusce eget neque elit. Sed augue orci, elementum in magna congue, tincidunt vulputate erat. Aliquam consectetur orci molestie dictum molestie. Proin eget congue nulla, vel tempor diam.</p>
<ul class="services">
  <li><svg width="24" height="24" viewBox="0 0 24 24"><circle cx="12" cy="12" r="12" fill="var(--blue)"/><path d="M6.5 12.5l4 4 7-8" fill="none" stroke="#fff" stroke-width="3"/></svg>Restaurants</li>
  <li><svg width="24" height="24" viewBox="0 0 24 24"><circle cx="12" cy="12" r="12" fill="var(--blue)"/><path d="M6.5 12.5l4 4 7-8" fill="none" stroke="#fff" stroke-width="3"/></svg>Real Estate</li>
  <li><svg width="24" height="24" viewBox="0 0 24 24"><circle cx="12" cy="12" r="12" fill="var(--blue)"/><path d="M6.5 12.5l4 4 7-8" fill="none" stroke="#fff" stroke-width="3"/></svg>Development</li>
</ul>
<div class="btn" style="left:641px;top:1722px;width:117px;height:43px">Read More</div>

<h2 class="section" style="left:0;width:1200px;text-align:center;top:1933px">News</h2>
<article class="card" style="left:144px">
  <div class="pic" role="img" aria-label="Photo of a restaurant dining area with plants" style="background:linear-gradient(135deg,#3a3024,#8a6a48)"></div>
  <div class="date">4 January, 2021</div>
  <div class="title">Maecenas vel tortor accumsan quam varius imperdiet vel eget tincidunt lectus.</div>
</article>
<article class="card" style="left:452px">
  <div class="pic" role="img" aria-label="Photo of a bar counter under pendant lights" style="background:linear-gradient(135deg,#1e3a4a,#4a6a7a)"></div>
  <div class="date">4 January, 2021</div>
  <div class="title">Etiam vel massa elementum, bibendum tellus venenatis, feugiat massa. Curabitur venenatis.</div>
</article>
<article class="card" style="left:759px">
  <div class="pic" role="img" aria-label="Photo of a restaurant with an open kitchen" style="background:linear-gradient(135deg,#6a4a30,#b0a090)"></div>
  <div class="date">4 January, 2021</div>
  <div class="title">Pellentesque convallis molestie enim sit amet efficitur imperdiet lectus euismod iaculis.</div>
</article>
<div class="btn" style="left:540px;top:2317px;width:119px;height:43px">View All</div>

<h2 class="section" style="left:143px;top:2490px">Contact us</h2>
<div class="field" style="left:143px;top:2547px;width:217px;height:39px">Name</div>
<div class="field" style="left:375px;top:2547px;width:217px;height:39px">Email</div>
<div class="field" style="left:143px;top:2603px;width:217px;height:39px">Phone</div>
<div class="field" style="left:375px;top:2603px;width:217px;height:39px">Title</div>
<div class="field" style="left:143px;top:2659px;width:449px;height:94px">Message</div>
<div class="btn" style="left:143px;top:2770px;width:119px;height:43px">Submit</div>

<div class="abs foot-links">Home &nbsp;| &nbsp;About us &nbsp;| &nbsp;Locations &nbsp;| &nbsp;News &nbsp;| &nbsp;Contact Us &nbsp;| &nbsp;Join the Team</div>
<div class="abs foot-copy">Copyright &nbsp;© &nbsp;2021 &nbsp;ORVA. &nbsp;All rights reserved.</div>

</body>
</html>
```